ZRD Roofing Billboard Design

Looking for a fresh new billboard design with my new headshot photo and using some info from my previous billboard and maybe website for design/content inspiration. My website is https://zrdroofing.com/

Also attached are my logo and current lawn sign design. I am looking for something simple, clean and modern. The landing page website should be 3816tops.com like my previous billboard has.

```html
<!DOCTYPE html>
<html lang="en">
<head>
<meta charset="utf-8">
<title>ZRD Roofing Billboard</title>
<link rel="stylesheet" href="https://fonts.googleapis.com/css2?family=League+Gothic&family=Arimo:wght@700&display=swap">
<style>
  :root {
    --stage: #959b9d;
    --white: #ffffff;
    --panel-light: #eeefef;
    --navy: #0c1d3b;
    --lime: #c6d941;
    --teal: #25778a;
    --sky: #2a9ee0;
    --sky-light: #9fd0f0;
    --roof-grey: #8e9fb5;
    --siding: #dfe4ea;
    --shirt-blue: #b4c3e2;
  }
  * { box-sizing: border-box; margin: 0; padding: 0; }
  html, body { width: 1200px; height: 473px; overflow: hidden; }
  body { background: var(--stage); position: relative; }

  .billboard {
    position: absolute; left: 45px; top: 68px;
    width: 1110px; height: 336px;
    background: linear-gradient(180deg, var(--white) 0%, var(--panel-light) 100%);
    overflow: hidden;
  }

  .brand-panel {
    position: absolute; left: 0; top: 0; width: 320px; height: 261px;
    background: var(--white);
    display: flex; flex-direction: column; align-items: center; justify-content: center; gap: 14px;
  }
  .brand-mark { width: 96px; height: 96px; border-radius: 50%; background: var(--lime); }
  .brand-name {
    font-family: "Arimo", Arial, sans-serif; font-weight: 700;
    font-size: 26px; color: var(--navy);
  }

  .phone-band {
    position: absolute; left: 0; top: 261px; width: 320px; height: 75px;
    background: var(--teal);
    display: flex; align-items: center; justify-content: center;
    font-family: "Arimo", Arial, sans-serif; font-weight: 700;
    font-size: 29px; color: var(--white); letter-spacing: 0.3px;
  }

  .headline {
    position: absolute; left: 362px; top: 12px;
    font-family: "League Gothic", "Arial Narrow", sans-serif; font-weight: 400;
    color: var(--navy); text-transform: uppercase; line-height: 1;
    text-shadow: -3px 3px 0 var(--lime);
  }
  .headline-main { display: block; font-size: 107px; height: 92px; letter-spacing: 1px; }
  .headline-sub { display: block; font-size: 66px; letter-spacing: 5.4px; }

  .price-intro {
    position: absolute; left: 362px; top: 193px;
    font-family: "League Gothic", "Arial Narrow", sans-serif;
    font-size: 35px; line-height: 1; color: var(--navy);
  }
  .price-box {
    position: absolute; left: 472px; top: 169px; width: 225px; height: 85px;
    background: var(--lime);
    clip-path: polygon(0 0, 100% 0, calc(100% - 26px) 100%, 0 100%);
    font-family: "League Gothic", "Arial Narrow", sans-serif;
    font-size: 88px; line-height: 85px; color: var(--navy);
    padding-left: 30px; letter-spacing: 1px;
  }

  .url-box {
    position: absolute; left: 362px; top: 261px; width: 302px; height: 75px;
    background: var(--navy);
    clip-path: polygon(0 0, 100% 0, calc(100% - 24px) 100%, 0 100%);
    font-family: "League Gothic", "Arial Narrow", sans-serif;
    font-size: 60px; line-height: 75px; color: var(--white);
    padding-left: 34px;
  }

  .photo-side { position: absolute; left: 0; top: 0; width: 1110px; height: 336px; }
</style>
</head>
<body>
  <main class="billboard">
    <section class="brand-panel">
      <div class="brand-mark"></div>
      <div class="brand-name">ZRD Roofing LLC</div>
    </section>
    <div class="phone-band">(555) 218-0473</div>

    <h1 class="headline">
      <span class="headline-main">Full Roof</span>
      <span class="headline-sub">Replacements</span>
    </h1>
    <p class="price-intro">Starting at</p>
    <div class="price-box">$3,816</div>
    <div class="url-box">3816tops.com</div>

    <svg class="photo-side" viewBox="0 0 1110 336">
      <defs>
        <linearGradient id="headshot-tones" x1="0" y1="0" x2="0.35" y2="1">
          <stop offset="0" stop-color="var(--sky-light)"/>
          <stop offset="0.3" stop-color="var(--roof-grey)"/>
          <stop offset="0.6" stop-color="var(--siding)"/>
          <stop offset="1" stop-color="var(--shirt-blue)"/>
        </linearGradient>
      </defs>
      <polygon class="accent-lime" points="747,0 758,0 656,336 640,336" fill="var(--lime)"/>
      <polygon class="accent-sky" points="758,0 765,0 663,336 656,336" fill="var(--sky)"/>
      <polygon class="headshot" role="img" aria-label="Headshot of the smiling roofer in a light blue shirt in front of a white-sided house with a grey shingle roof" points="765,0 1110,0 1110,336 663,336" fill="url(#headshot-tones)"/>
    </svg>
  </main>
</body>
</html>
```